Business Card Design

I need a Business Card that will catch the attention that will not get thrown in a Drawer. I have 23 companies I use for Auto, Home, Life, and Business Insurance. I make sure that people have the best coverage for the $ spent.

Industry/Entity Type

Business

Contact Information for Business Card

Dorlin Insurance Agency, Inc., Marcus Helgren, 4375 West Tamber Lane Corvale, Westmark 45192 555-281-7496, www.dorlinagency.example, Facebook, LinkedIn, Google+

```html
<!DOCTYPE html>
<html lang="en">
<head>
<meta charset="utf-8">
<title>Dorlin Insurance Agency – Business Card</title>
<link href="https://fonts.googleapis.com/css2?family=Open+Sans:wght@400;600;700&display=swap" rel="stylesheet">
<style>
  :root {
    --bg: #e4e4e4;
    --card: #ffffff;
    --ink: #3f3f3f;
    --ink-soft: #5a5a5a;
    --accent: #6cb7d5;
    --band: #383838;
    --divider: #ececec;
    --icon-fill: #4a4a4a;
  }
  * { margin: 0; padding: 0; box-sizing: border-box; }
  html, body {
    width: 1200px; height: 800px; overflow: hidden;
    background: var(--bg);
    font-family: "Open Sans", Arial, sans-serif;
    color: var(--ink);
  }
  .sheet {
    width: 1200px; height: 800px;
    display: flex; align-items: center; justify-content: center; gap: 60px;
  }
  .card {
    position: relative;
    width: 520px; height: 297px;
    background: var(--card);
    overflow: hidden;
    box-shadow: 0 6px 18px rgba(0,0,0,0.12);
  }
  .card__swoosh {
    position: absolute; left: 0; top: 0; width: 100%; height: 100%;
  }
  .swoosh__accent { fill: var(--accent); }
  .swoosh__band { fill: var(--band); }

  /* Contact side */
  .contact {
    position: absolute; left: 0; right: 0; top: 50px;
    display: flex; flex-direction: column; align-items: center;
    text-align: center;
  }
  .contact__identity { display: inline-flex; flex-direction: column; }
  .contact__name {
    font-size: 30px; font-weight: 700; letter-spacing: 1px;
    text-transform: uppercase; color: var(--ink-soft);
    padding-bottom: 2px;
    border-bottom: 1px solid var(--accent);
    line-height: 1.15;
  }
  .contact__role {
    align-self: flex-end;
    font-size: 12px; font-weight: 600; color: var(--ink-soft);
    margin-top: 3px;
  }
  .contact__address {
    margin-top: 22px;
    font-size: 15px; font-weight: 600; line-height: 1.35;
  }
  .contact__phone {
    margin-top: 10px;
    font-size: 23px; font-weight: 700; letter-spacing: 0.5px;
  }

  /* Company side */
  .brand {
    position: absolute; left: 0; right: 0; top: 62px;
    text-align: center;
  }
  .brand__name { font-size: 26px; font-weight: 700; color: var(--ink-soft); }
  .brand__url { font-size: 15px; font-weight: 700; color: var(--accent); margin-top: 1px; }

  .services {
    position: absolute; left: 22px; right: 22px; top: 138px;
    display: flex; list-style: none;
  }
  .service {
    flex: 1;
    display: flex; flex-direction: column; align-items: center;
    padding: 0 6px;
    border-right: 1px solid var(--divider);
  }
  .service:last-child { border-right: none; }
  .service__icon {
    width: 34px; height: 30px;
    background: var(--icon-fill);
    border-radius: 3px;
  }
  .service__label {
    margin-top: 6px;
    font-size: 9px; font-weight: 600; line-height: 1.2;
    color: var(--accent); text-align: center;
  }
</style>
</head>
<body>
<main class="sheet">

  <section class="card card--contact" aria-label="Business card, contact side">
    <svg class="card__swoosh" viewBox="0 0 520 297" preserveAspectRatio="none" aria-hidden="true">
      <path class="swoosh__accent" d="M0,258 Q280,268 520,232 L520,297 L0,297 Z"/>
      <path class="swoosh__band" d="M0,267 Q280,277 520,241 L520,297 L0,297 Z"/>
    </svg>
    <div class="contact">
      <div class="contact__identity">
        <h1 class="contact__name">Marcus Helgren</h1>
        <p class="contact__role">Company Position</p>
      </div>
      <p class="contact__address">4375 West Tamber Lane Corvale,<br>Westmark 45192</p>
      <p class="contact__phone">555-281-7496</p>
    </div>
  </section>

  <section class="card card--company" aria-label="Business card, company side">
    <svg class="card__swoosh" viewBox="0 0 520 297" preserveAspectRatio="none" aria-hidden="true">
      <path class="swoosh__accent" d="M0,256 Q300,262 520,214 L520,297 L0,297 Z"/>
      <path class="swoosh__band" d="M0,266 Q300,272 520,225 L520,297 L0,297 Z"/>
    </svg>
    <div class="brand">
      <h2 class="brand__name">Dorlin Insurance Agency, Inc.</h2>
      <p class="brand__url">www.dorlinagency.example</p>
    </div>
    <ul class="services">
      <li class="service">
        <div class="service__icon" role="img" aria-label="House icon"></div>
        <span class="service__label">Home &amp; Auto<br>Insurance</span>
      </li>
      <li class="service">
        <div class="service__icon" role="img" aria-label="Construction crane icon"></div>
        <span class="service__label">Construction<br>Insurance</span>
      </li>
      <li class="service">
        <div class="service__icon" role="img" aria-label="Office building icon"></div>
        <span class="service__label">Commercial<br>General Liability</span>
      </li>
      <li class="service">
        <div class="service__icon" role="img" aria-label="Family icon"></div>
        <span class="service__label">Individual Life<br>Insurance</span>
      </li>
      <li class="service">
        <div class="service__icon" role="img" aria-label="Shield icon"></div>
        <span class="service__label">Other Services</span>
      </li>
    </ul>
  </section>

</main>
</body>
</html>
```